Business school needs a web design

Who We are:
KRVT is a small business school that offers programs in Project Management. The school is based in West Africa and welcomes students from the whole area. Our aim is to become one of the reference business schools in Africa.

Project Brief:
The site will include all informations relevant for different types of visitors that we have: actual and future students, companies, mass media, future employees, ect. It will present information about subscription, list of programs, presentation of the school and its team,etc.

What We want:
This competition is for Design only no coding! We need design for two pages.
We did some wireframing for the home page and the list of programs page. We made them just to show how we imagine the website would look like. But we encourage creative designs, so you don't have to stick to the wireframe models.

Sites We like:
http://www.ravenmoorcollege.example/
http://www.belvantis.example/fr/etudes.html
http://www.qtl.example/mba/Pages/default.aspx

Color schemes
The logo of the school is red and black. So the color scheme of the website should match that. For the rest, it is opened to your imagination.
Updates

The payment for the project is now garanteed. Good luck to you all !

Target Market(s)

The target market is diversified because we have students of different ages, also company representatives or employees that might visit the website for recruitment purposes. But the majority of our audience should be aged between 20 - 30 years.

Industry/Entity Type

Small Business

Requirements
Must have
• The design must include two pages: a home page and another interior page : might be the list of programs or any other page relevant to the domain. The Home page must include a slide show at the beginning.
The background page must be white.
Nice to have
• The use of flat design for this project is preferred.
The use of Pelican scaffold as a base for the design is an asset.

```html
<!DOCTYPE html>
<html lang="fr">
<head>
<meta charset="utf-8">
<title>KRVT – École de gestion de projet</title>
<link href="https://fonts.googleapis.com/css2?family=Roboto:wght@400;500;700&family=Roboto+Condensed:wght@400;700&display=swap" rel="stylesheet">
<style>
:root{
  --red:#d21f26;
  --red-dark:#a9151b;
  --ink:#222;
  --text:#555;
  --muted:#8a8a8a;
  --line:#e2e2e2;
  --nav:#3b3b3d;
  --nav-line:#2c2c2e;
  --panel:#f4f4f4;
  --white:#fff;
  --footer-bar:#2a2a2a;
}
*{box-sizing:border-box;margin:0;padding:0}
html,body{width:896px;height:1200px;overflow:hidden;background:var(--white)}
body{font-family:"Roboto",Arial,sans-serif;color:var(--text);font-size:10px;position:relative}
a{color:inherit;text-decoration:none}
ul{list-style:none}

/* header */
.site-header{position:absolute;left:0;top:0;width:896px;height:118px}
.brand{position:absolute;left:90px;top:10px;display:flex;align-items:center;gap:10px}
.brand-mark{width:46px;height:46px;background:var(--red)}
.brand-name{font:700 30px "Roboto",sans-serif;color:var(--ink);letter-spacing:1px}
.utility{position:absolute;right:38px;top:8px;display:flex;gap:5px}
.utility a{background:var(--red);color:var(--white);font-size:9px;font-weight:500;padding:4px 7px;border-radius:2px}
.callus{position:absolute;right:38px;top:42px;display:flex;align-items:center;gap:8px}
.callus .icon{width:32px;height:32px;border-radius:50%;background:var(--red);display:flex;align-items:center;justify-content:center}
.callus small{display:block;font-size:10px;color:var(--muted)}
.callus strong{font:700 22px "Roboto Condensed",sans-serif;color:var(--red)}
.main-nav{position:absolute;left:0;top:96px;width:896px;height:26px;background:var(--nav);border-bottom:2px solid var(--nav-line);display:flex;padding-left:85px}
.main-nav a{color:#eee;font-size:10px;font-weight:500;line-height:26px;padding:0 13px}
.main-nav a.active{background:var(--red);color:var(--white)}

/* slider */
.hero{position:absolute;left:0;top:122px;width:896px;height:310px;background:linear-gradient(100deg,#d9dde2 0%,#f2f2f2 35%,#c9ccd1 62%,#6f7479 100%)}
.hero-caption{position:absolute;left:0;bottom:22px;width:896px;height:36px;background:rgba(20,20,20,.6);color:var(--white);font:500 19px "Roboto",sans-serif;line-height:36px;padding-left:50px}
.hero-arrow{position:absolute;top:130px;width:26px;height:40px;background:rgba(0,0,0,.35);display:flex;align-items:center;justify-content:center}
.hero-arrow.prev{left:0}.hero-arrow.next{right:0}
.hero-dots{position:absolute;right:34px;bottom:34px;display:flex;gap:6px}
.hero-dots span{width:10px;height:10px;border-radius:50%;background:var(--white)}
.hero-dots span.on{background:var(--red)}

/* content */
.content{position:absolute;left:85px;top:448px;width:775px;height:475px}
.section-title{display:flex;align-items:center;gap:8px;font:700 15px "Roboto Condensed",sans-serif;color:var(--red);margin-bottom:8px}
.section-title .ico{width:20px;height:20px;background:var(--ink);border-radius:3px;flex:none}
.more{display:inline-block;background:var(--red);color:var(--white);font-size:8px;padding:2px 7px}
.readlink{font-size:8px;color:var(--red);font-weight:500;border-bottom:1px solid var(--red)}

.audience{position:absolute;left:0;top:0;width:165px}
.audience .section-title{color:var(--ink);font-size:17px}
.audience .section-title .ico{background:none}
.audience li{font-size:11px;color:var(--text);padding:3px 0 3px 12px;position:relative}
.audience li::before{content:"";position:absolute;left:0;top:7px;border-left:5px solid var(--red);border-top:4px solid transparent;border-bottom:4px solid transparent}
.tv{position:absolute;left:0;top:196px;width:165px}
.tv .section-title .ico{background:var(--red);border-radius:50%}
.tv-player{height:92px;background:linear-gradient(135deg,#5a5a5a,#9a9a9a);position:relative;display:flex;align-items:center;justify-content:center}
.tv-controls{position:absolute;left:0;bottom:0;width:100%;height:10px;background:#111}
.tv a{display:block;margin-top:5px;font-size:9px;color:var(--ink)}

.center{position:absolute;left:190px;top:0;width:335px}
.center p{font-size:9px;line-height:1.45;color:var(--text)}
.intro{border-bottom:1px solid var(--line);padding-bottom:8px;margin-bottom:12px}
.intro .more{float:right;margin-top:4px}
.blog-list{display:flex;gap:12px;border-bottom:1px solid var(--line);padding-bottom:10px;margin-bottom:12px}
.blog-card{width:100px}
.blog-card .thumb{height:58px;background:linear-gradient(135deg,#cfd3d8,#8e9398);margin-bottom:4px}
.blog-card .date{font-size:8px;color:var(--red);font-weight:700}
.blog-card h4{font-size:9px;color:var(--ink)}
.blog-card p{font-size:8px!important;margin-bottom:3px}
.event{display:flex;gap:10px;margin-bottom:10px}
.event .cal{width:38px;height:38px;background:var(--panel);border:1px solid var(--line);flex:none;text-align:center}
.event .cal b{display:block;background:var(--red);color:var(--white);font-size:8px;line-height:12px}
.event .cal span{font:700 15px "Roboto Condensed",sans-serif;color:var(--ink);line-height:24px}
.all-events{text-align:right}

.news{position:absolute;left:545px;top:0;width:230px}
.news li{display:flex;gap:8px;padding:7px 0;border-bottom:1px solid var(--line)}
.news .thumb{width:60px;height:44px;background:linear-gradient(135deg,#d2d5d9,#7d8186);flex:none}
.news p{font-size:9px;line-height:1.35;color:var(--text)}

.share-rail{position:absolute;right:0;top:580px;width:22px;background:var(--panel);display:flex;flex-direction:column;gap:4px;padding:4px 3px}
.share-rail span{width:16px;height:16px;background:#7c7c7c;border-radius:2px}

/* partners */
.partners{position:absolute;left:90px;top:935px;width:730px;height:58px;display:flex;justify-content:space-around;align-items:center;border-top:1px solid var(--line)}
.partners span{width:120px;height:30px;background:#c9ccd0;border-radius:4px}
.partners span:nth-child(2){background:#9ea3a8}

/* footer */
.site-footer{position:absolute;left:0;top:1005px;width:896px;height:195px;background:var(--red);color:var(--white)}
.footer-cols{display:flex;gap:22px;padding:14px 0 0 85px}
.footer-cols h5{font:700 12px "Roboto Condensed",sans-serif;margin-bottom:8px}
.footer-cols li{font-size:9px;line-height:1.6;color:#fbe3e3}
.follow li{display:flex;align-items:center;gap:6px;margin-bottom:3px}
.follow li i{width:14px;height:14px;background:var(--white);border-radius:2px;display:block}
.contact li{display:flex;gap:6px;align-items:flex-start}
.newsletter p{font-size:9px;line-height:1.5;color:#fbe3e3;margin-bottom:8px}
.newsletter .field{display:flex}
.newsletter .field span{width:90px;height:18px;background:var(--white)}
.newsletter .field b{background:var(--footer-bar);font-size:8px;line-height:18px;padding:0 8px;font-weight:500}
.footer-bar{position:absolute;left:0;bottom:0;width:896px;height:22px;background:var(--red-dark);text-align:center;font-size:9px;line-height:22px;color:#fbe3e3}
</style>
</head>
<body>

<header class="site-header">
  <a class="brand" href="#"><span class="brand-mark"></span><span class="brand-name">KRVT</span></a>
  <nav class="utility">
    <a href="#">Répertoire du personnel</a><a href="#">Blogue</a><a href="#">Boîte de poste</a><a href="#">Nous joindre</a><a href="#">Français</a>
  </nav>
  <div class="callus">
    <span class="icon"><svg width="16" height="16" viewBox="0 0 24 24"><path fill="#fff" d="M6.6 10.8a15 15 0 0 0 6.6 6.6l2.2-2.2c.3-.3.7-.4 1-.2 1.1.4 2.3.6 3.6.6.6 0 1 .4 1 1V20c0 .6-.4 1-1 1A17 17 0 0 1 3 4c0-.6.4-1 1-1h3.5c.6 0 1 .4 1 1 0 1.3.2 2.5.6 3.6.1.3 0 .7-.2 1z"/></svg></span>
    <div><small>Call us</small><strong>(221) 33 000 41 27</strong></div>
  </div>
  <nav class="main-nav">
    <a class="active" href="#">À Propos de KRVT</a><a href="#">Programmes et Formations</a><a href="#">Étudiants</a><a href="#">Nouvelles et Événements</a><a href="#">Entreprises</a>
  </nav>
</header>

<section class="hero" role="img" aria-label="Photo de diaporama : une formatrice présente devant un tableau à un groupe de participants en salle de réunion">
  <span class="hero-arrow prev"><svg width="10" height="16"><path d="M8 2 2 8l6 6" stroke="#fff" stroke-width="2" fill="none"/></svg></span>
  <span class="hero-arrow next"><svg width="10" height="16"><path d="m2 2 6 6-6 6" stroke="#fff" stroke-width="2" fill="none"/></svg></span>
  <div class="hero-caption">Lorem Ipsum lorem ipsum delit lorem Ipsum lorem</div>
  <div class="hero-dots"><span class="on"></span><span></span><span></span><span></span></div>
</section>

<main class="content">
  <aside class="audience">
    <h3 class="section-title"><span class="ico"><svg width="20" height="20" viewBox="0 0 20 20"><circle cx="10" cy="10" r="6" fill="none" stroke="#222" stroke-width="4" stroke-dasharray="3 2"/><circle cx="10" cy="10" r="2.5" fill="#222"/></svg></span>Vous êtes</h3>
    <ul>
      <li>Futur étudiant</li><li>Étudiant actuel</li><li>Entreprise</li><li>Employeur</li><li>Postulant</li><li>Médias</li><li>Partenaires</li>
    </ul>
  </aside>
  <aside class="tv">
    <h3 class="section-title"><span class="ico"></span>KRVT.tv</h3>
    <div class="tv-player" role="img" aria-label="Vidéo de présentation de l'école">
      <svg width="26" height="26"><circle cx="13" cy="13" r="12" fill="rgba(0,0,0,.5)"/><path d="M10 7v12l9-6z" fill="#fff"/></svg>
      <span class="tv-controls"></span>
    </div>
    <a href="#">› les vidéos</a>
  </aside>

  <section class="center">
    <div class="intro">
      <h3 class="section-title"><span class="ico"></span>Devenez Les Gestionnaires De Demain</h3>
      <p>Lorem ipsum dolor sit amet, consectetur adipiscing elit, sed do eiusmod tempor incididunt ut labore et dolore magna aliqua.</p>
      <a class="more" href="#">Lire plus</a>
      <div style="clear:both"></div>
    </div>
    <h3 class="section-title"><span class="ico"></span>Blogue</h3>
    <div class="blog-list">
      <article class="blog-card"><div class="thumb" role="img" aria-label="Photo d'article de blogue"></div><div class="date">Jan 11, 2014</div><h4>Titre</h4><p>Lorem ipsum dolor sit amet.</p><a class="readlink" href="#">Lire la suite</a></article>
      <article class="blog-card"><div class="thumb" role="img" aria-label="Photo d'article de blogue"></div><div class="date">Jan 11, 2014</div><h4>Titre</h4><p>Lorem ipsum dolor sit amet.</p><a class="readlink" href="#">Lire la suite</a></article>
      <article class="blog-card"><div class="thumb" role="img" aria-label="Photo d'article de blogue"></div><div class="date">Jan 11, 2014</div><h4>Titre</h4><p>Lorem ipsum dolor sit amet.</p><a class="readlink" href="#">Lire la suite</a></article>
    </div>
    <h3 class="section-title"><span class="ico"></span>Événements</h3>
    <div class="event"><div class="cal"><b>JAN</b><span>14</span></div><div><p>Lorem ipsum dolor sit amet, consectetur adipiscing elit sed do.</p><a class="readlink" href="#">Lire la suite</a></div></div>
    <div class="event"><div class="cal"><b>JAN</b><span>22</span></div><div><p>Lorem ipsum dolor sit amet, consectetur adipiscing elit sed do.</p><a class="readlink" href="#">Lire la suite</a></div></div>
    <p class="all-events"><a class="readlink" href="#">Tous les Événements</a></p>
  </section>

  <section class="news">
    <h3 class="section-title"><span class="ico"></span>Nouvelles</h3>
    <ul>
      <li><div class="thumb" role="img" aria-label="Photo de nouvelle"></div><p>Lorem ipsum Dolor Sit<br><a class="readlink" href="#">Lire la suite</a></p></li>
      <li><div class="thumb" role="img" aria-label="Photo de nouvelle"></div><p>Lorem ipsum Dolor Sit<br><a class="readlink" href="#">Lire la suite</a></p></li>
      <li><div class="thumb" role="img" aria-label="Photo de nouvelle"></div><p>Lorem ipsum Dolor Sit<br><a class="readlink" href="#">Lire la suite</a></p></li>
      <li><div class="thumb" role="img" aria-label="Photo de nouvelle"></div><p>Lorem ipsum Dolor Sit<br><a class="readlink" href="#">Lire la suite</a></p></li>
      <li><div class="thumb" role="img" aria-label="Photo de nouvelle"></div><p>Lorem ipsum Dolor Sit<br><a class="readlink" href="#">Lire la suite</a></p></li>
    </ul>
  </section>
</main>

<div class="share-rail"><span></span><span></span><span></span><span></span><span></span><span></span></div>

<section class="partners" aria-label="Partenaires"><span></span><span></span><span></span><span></span></section>

<footer class="site-footer">
  <div class="footer-cols">
    <div class="follow" style="width:110px">
      <h5>Suivez - nous &gt;&gt;</h5>
      <ul><li><i></i>Cercle</li><li><i></i>Chirp</li><li><i></i>ProLink</li><li><i></i>ViewTube</li></ul>
    </div>
    <div style="width:115px">
      <h5>À propos</h5>
      <ul><li>À propos de KRVT</li><li>Admissions</li><li>Contactez-nous</li><li>Offre d'emploi</li><li>Répertoire du personnel</li></ul>
    </div>
    <div style="width:125px">
      <h5>Étudiants</h5>
      <ul><li>Accueil - Étudiants</li><li>Programmes et Formations</li><li>Vie étudiante</li><li>Entreprises</li><li>Médias</li></ul>
    </div>
    <div class="contact" style="width:150px">
      <h5>KRVT</h5>
      <ul><li>12, Rue des Acacias, Immeuble Baobab, Dakar</li><li>(221) 33 000 41 27</li><li>(221) 77 000 58 63</li></ul>
    </div>
    <div class="newsletter" style="width:150px">
      <h5>Infolettre</h5>
      <p>Recevez nos dernières nouvelles et événements directement dans votre boîte.</p>
      <div class="field"><span></span><b>Envoyer</b></div>
    </div>
  </div>
  <div class="footer-bar">© 2014 KRVT. Tous droits réservés</div>
</footer>

</body>
</html>
```